Gelato Business Card

create a new business card using existing logo

Target Market(s)

B2B

Contact Information for Business Card

typical contact info: logo, address, email, phone, rep name

Colors
0355a3
33a6d7

Requirements
Must have
• a feel of high quality, luxury, happiness
• use cool, comforting color and texture of business card.
Nice to have
• "A Little Perfection Goes A Long Way!" TM
• or, "more quality, more flavor"
• or, "Flavor Matters"

```html
<!DOCTYPE html>
<html lang="en">
<head>
<meta charset="utf-8">
<title>Bellamare Gelato – Business Card</title>
<link rel="stylesheet" href="https://fonts.googleapis.com/css2?family=Jost:wght@400&display=swap">
<style>
  :root {
    --card-bg: #ffffff;
    --ink-blue: #1a47e8;
    --wave-deep: #0a45f5;
    --wave-light: #4dd0f2;
    --page-bg: #ffffff;
  }
  html, body {
    margin: 0;
    padding: 0;
    width: 1200px;
    height: 734px;
    overflow: hidden;
    background: var(--page-bg);
  }
  .business-card {
    position: relative;
    width: 1200px;
    height: 734px;
    background: var(--card-bg);
    overflow: hidden;
    font-family: "Jost", "Futura", sans-serif;
    color: var(--ink-blue);
  }
  .brand-name {
    position: absolute;
    left: 56px;
    top: 76px;
    margin: 0;
    display: flex;
    align-items: center;
    gap: 14px;
    font-size: 38px;
    font-weight: 400;
    letter-spacing: 1px;
    color: var(--wave-deep);
  }
  .brand-dot {
    width: 26px;
    height: 26px;
    border-radius: 50%;
    background: var(--wave-deep);
  }
  .contact-block {
    position: absolute;
    right: 57px;
    top: 196px;
    width: 436px;
    text-align: right;
    font-weight: 400;
  }
  .rep-name {
    margin: 0;
    font-size: 52px;
    line-height: 1;
    font-weight: 400;
    padding-bottom: 16px;
    border-bottom: 3px solid var(--ink-blue);
  }
  .rep-position {
    margin: 12px 0 0;
    font-size: 47px;
    line-height: 1.1;
  }
  .address {
    margin: 26px 0 0;
    font-size: 35px;
    line-height: 46px;
    font-style: normal;
  }
  .phone {
    margin: 24px 0 0;
    font-size: 38px;
    line-height: 1.2;
  }
  .email {
    margin: 8px 0 0;
    font-size: 35px;
    line-height: 1.2;
  }
  .wave-artwork {
    position: absolute;
    left: 46px;
    right: 9px;
    bottom: 0;
    height: 140px;
    border-top-left-radius: 220px 140px;
    background: linear-gradient(90deg, var(--wave-deep) 0%, var(--wave-deep) 55%, var(--wave-light) 100%);
  }
</style>
</head>
<body>
  <main class="business-card">
    <h1 class="brand-name"><span class="brand-dot"></span>Bellamare Gelato</h1>

    <section class="contact-block">
      <h2 class="rep-name">Your Name Here</h2>
      <p class="rep-position">Position</p>
      <address class="address">Address 1<br>Address 2</address>
      <p class="phone">+1 876 5432 100</p>
      <p class="email">mailto@yourmail.com</p>
    </section>

    <div class="wave-artwork" role="img" aria-label="Decorative artwork of overlapping deep blue and light cyan waves along the bottom edge"></div>
  </main>
</body>
</html>
```